Quillmora Name Card & Logo Design

We need a new business card design and a logo for our company as well. Our company is in the computer retail business. We provide our walk in customers with a wide range of computer products from mouse to complete desktop.Anything you need in a computer? We got it. Our area of aim is to provide customers with value and trust in our service & products .We provide customization of Computer desktop/ Repairs of laptop/desktop.
You may want to take a look at our Website for more information.
www.quillmora.com.sg
Industry/Entity Type
Computer
Contact Information for Business Card
Quillmora Systems
Tan Bei Lorn
Operations Manager
+65 6480 2917
+65 9264 3085
tanbl@quillmora.com.sg
Corporate Sales Enquries : corporatesales@quillmora.com.sg

```html
<!DOCTYPE html>
<html lang="en">
<head>
<meta charset="utf-8">
<title>Quillmora Systems – Name Card</title>
<link rel="stylesheet" href="https://fonts.googleapis.com/css2?family=Questrial&display=swap">
<style>
  :root {
    --bg: #e4e4e4;
    --card-white: #ffffff;
    --sky: #9fd8f4;
    --sky-light: #d4efff;
    --sky-deep: #63bde9;
    --navy: #33338f;
    --brand: #1e8fd6;
    --ink: #2b2b2b;
    --rule: #8a8a8a;
  }
  * { margin: 0; padding: 0; box-sizing: border-box; }
  html, body { width: 1200px; height: 750px; overflow: hidden; }
  body {
    background: var(--bg);
    font-family: "Questrial", "Century Gothic", sans-serif;
    color: var(--ink);
    position: relative;
  }
  .card {
    position: absolute;
    top: 225px;
    width: 510px;
    height: 300px;
    border-radius: 14px;
    overflow: hidden;
    box-shadow: 0 6px 18px rgba(0,0,0,0.12);
  }
  /* Front */
  .card--front { left: 55px; background: var(--card-white); }
  .brand {
    position: absolute;
    display: flex;
    align-items: center;
    gap: 10px;
  }
  .brand__dot {
    width: 26px; height: 26px; border-radius: 50%;
    background: var(--brand);
  }
  .brand__name {
    font-size: 24px;
    color: var(--brand);
    text-transform: uppercase;
    letter-spacing: 1px;
    line-height: 1;
  }
  .card--front .brand { left: 40px; top: 82px; }
  .front__rule {
    position: absolute;
    left: 40px; right: 40px; top: 135px;
    height: 1px; background: var(--rule);
  }
  .person {
    position: absolute; right: 40px; top: 58px; text-align: right;
  }
  .person__name { font-size: 20px; color: var(--navy); }
  .person__title { font-size: 10px; font-weight: bold; color: var(--ink); margin-top: 3px; }
  .phones {
    position: absolute; left: 40px; top: 160px;
    display: flex; align-items: center; gap: 10px;
    font-size: 12px; line-height: 1.35;
  }
  .emails {
    position: absolute; right: 40px; top: 148px; text-align: right;
    font-size: 12px; line-height: 1.5;
  }
  .emails__line { display: flex; align-items: center; justify-content: flex-end; gap: 6px; }
  .icon { width: 14px; height: 14px; fill: var(--ink); flex: none; }
  .front__bands { position: absolute; left: 0; bottom: 0; width: 510px; height: 90px; }
  /* Back */
  .card--back {
    left: 635px;
    background: radial-gradient(ellipse at 50% 38%, var(--sky-light) 0%, var(--sky) 55%, var(--sky-deep) 130%);
  }
  .card--back .brand {
    left: 0; right: 0; top: 112px; justify-content: center;
  }
  .card--back .brand__dot { background: #ffffff; width: 34px; height: 34px; }
  .card--back .brand__name { color: #ffffff; font-size: 32px; }
  .back__rule {
    position: absolute; left: 0; right: 0; top: 212px;
    height: 1px; background: rgba(255,255,255,0.85);
  }
  .tagline {
    position: absolute; left: 0; right: 0; top: 226px;
    text-align: center; font-size: 11px; color: #ffffff; letter-spacing: 0.3px;
  }
</style>
</head>
<body>
  <section class="card card--front">
    <div class="brand">
      <span class="brand__dot"></span>
      <span class="brand__name">Quillmora Systems</span>
    </div>
    <div class="front__rule"></div>

    <div class="person">
      <p class="person__name">Tan Bei Lorn</p>
      <p class="person__title">Operations Manager</p>
    </div>

    <div class="phones">
      <svg class="icon" viewBox="0 0 24 24" aria-hidden="true"><path d="M6.6 10.8a15.1 15.1 0 0 0 6.6 6.6l2.2-2.2c.3-.3.7-.4 1-.2 1.1.4 2.3.6 3.6.6.6 0 1 .4 1 1V20c0 .6-.4 1-1 1A17 17 0 0 1 3 4c0-.6.4-1 1-1h3.5c.6 0 1 .4 1 1 0 1.3.2 2.5.6 3.6.1.3 0 .7-.2 1z"/></svg>
      <div>
        <p>+65 6480 2917</p>
        <p>+65 9264 3085</p>
      </div>
    </div>

    <div class="emails">
      <p class="emails__line">
        <svg class="icon" viewBox="0 0 24 24" aria-hidden="true"><path d="M2 5h20v14H2z M4 7v.4l8 5 8-5V7z" fill-rule="evenodd"/></svg>
        <span>tanbl@quillmora.com.sg</span>
      </p>
      <p>corporatesales@quillmora.com.sg</p>
    </div>

    <svg class="front__bands" viewBox="0 0 510 90" preserveAspectRatio="none" aria-hidden="true">
      <polygon points="0,72 510,8 510,90 0,90" fill="var(--sky)"/>
      <polygon points="0,80 470,22 510,22 510,36 0,88" fill="var(--navy)"/>
    </svg>
  </section>

  <section class="card card--back">
    <div class="brand">
      <span class="brand__dot"></span>
      <span class="brand__name">Quillmora Systems</span>
    </div>
    <div class="back__rule"></div>
    <p class="tagline">We strive to serve you well since 1995</p>
  </section>
</body>
</html>
```